Lomi Vardell
Incorporated
Lomi Vardell -
Creative Brief
Use specific fonts
Please use font that would fulfill the requirements of the comment description below
Professional
Derek Holm
Operations Manager
City of Ashmere, CA
lomivardell@quillmesh.net
Our company extracts essential and fragrance oil from flowers. We blend our own brand-name perfume and fragrances. Please design cards to reflect a corporate appeal, with feminine luxury, higher end sophistication, yet gentle and soft. Attached is chosen logo. Feel free to take the abstract symbol and name out of the background if deemed necessary.

```html
<!DOCTYPE html>
<html lang="en">
<head>
<meta charset="utf-8">
<title>Lomi Vardell – Business Cards</title>
<link href="https://fonts.googleapis.com/css2?family=Cormorant+Garamond:wght@400;500&family=Lato:wght@400&display=swap" rel="stylesheet">
<style>
  :root {
    --bg: #e9e6e1;
    --gold-deep: #8a6a2c;
    --gold-mid: #b8944f;
    --gold-light: #e6cf94;
    --gold-text: #5e4418;
    --cream: #f7f0cc;
    --cream-soft: #efe4b4;
    --brown-text: #6b5226;
  }
  * { margin: 0; padding: 0; box-sizing: border-box; }
  html, body { width: 1200px; height: 814px; overflow: hidden; }
  body { background: var(--bg); position: relative; }

  .card {
    position: absolute;
    width: 520px;
    height: 300px;
    box-shadow: 0 8px 24px rgba(0,0,0,0.25);
    overflow: hidden;
  }

  /* Front card: gold */
  .card--front {
    left: 80px; top: 130px;
    background: radial-gradient(ellipse at 55% 30%, var(--gold-light) 0%, var(--gold-mid) 45%, var(--gold-deep) 100%);
  }
  .card--front .sheen {
    position: absolute; inset: 0;
    background: radial-gradient(ellipse 60% 45% at 20% 10%, rgba(255,240,200,0.3), rgba(255,240,200,0) 100%);
  }
  .brand-mark {
    position: absolute;
    width: 44px; height: 44px; border-radius: 50%;
  }
  .card--front .brand-mark {
    left: 278px; top: 40px;
    background: radial-gradient(circle at 40% 35%, #fff3cf, #c9a660 70%);
  }
  .brand-name {
    position: absolute;
    font-family: "Cormorant Garamond", serif;
    font-weight: 500;
    text-transform: uppercase;
    letter-spacing: 0.28em;
    white-space: nowrap;
  }
  .card--front .brand-name {
    left: 200px; top: 98px; width: 200px; text-align: center;
    font-size: 17px; color: var(--gold-text);
  }
  .contact-list {
    position: absolute; left: 250px; top: 140px;
    list-style: none;
    font-family: "Lato", sans-serif; font-size: 10px; color: var(--gold-text);
  }
  .contact-list li { display: flex; align-items: center; gap: 7px; height: 17px; white-space: nowrap; }
  .contact-list svg { width: 10px; height: 10px; fill: var(--gold-text); flex: none; }
  .person {
    position: absolute; left: 34px; top: 220px;
    color: var(--gold-text);
  }
  .person-name {
    font-family: "Cormorant Garamond", serif; font-size: 17px;
    text-transform: uppercase; letter-spacing: 0.04em;
  }
  .person-title {
    font-family: "Lato", sans-serif; font-size: 9px; opacity: 0.8; margin-top: 2px;
  }

  /* Back card: cream */
  .card--back {
    left: 600px; top: 380px;
    background: var(--cream);
  }
  .card--back .pattern {
    position: absolute; inset: 0;
    background: radial-gradient(ellipse at 50% 40%, var(--cream) 0%, var(--cream-soft) 100%);
  }
  .card--back .brand-mark {
    left: 238px; top: 50px;
    background: radial-gradient(circle at 40% 35%, #e9cf8c, var(--gold-deep) 80%);
  }
  .card--back .brand-name {
    left: 0; top: 110px; width: 520px; text-align: center;
    font-size: 17px; color: var(--brown-text);
  }
  .rule {
    position: absolute; left: 0; top: 166px; width: 520px; height: 2px;
    background: var(--gold-mid);
  }
  .email-band {
    position: absolute; left: 0; top: 176px; width: 520px; height: 38px;
    background: linear-gradient(90deg, var(--gold-deep), var(--gold-light) 50%, var(--gold-deep));
    display: flex; align-items: center; justify-content: center;
    font-family: "Lato", sans-serif; font-size: 12px; color: var(--cream);
    letter-spacing: 0.03em;
  }
</style>
</head>
<body>

  <section class="card card--front">
    <div class="sheen" role="img" aria-label="Soft flowing decorative lines"></div>
    <div class="brand-mark"></div>
    <div class="brand-name">Lomi Vardell</div>
    <ul class="contact-list">
      <li><svg viewBox="0 0 10 10"><path d="M5 0a3.5 3.5 0 0 0-3.5 3.5C1.5 6 5 10 5 10s3.5-4 3.5-6.5A3.5 3.5 0 0 0 5 0zm0 5a1.4 1.4 0 1 1 0-2.8A1.4 1.4 0 0 1 5 5z"/></svg>City of Ashmere, CA</li>
      <li><svg viewBox="0 0 10 10"><path d="M2 0h2l1 2.5-1.3 1a6 6 0 0 0 2.8 2.8l1-1.3L10 6v2a2 2 0 0 1-2 2A8 8 0 0 1 0 2a2 2 0 0 1 2-2z"/></svg>(949) 555-0182</li>
      <li><svg viewBox="0 0 10 10"><path d="M0 2h10v6H0zM0 2l5 3.5L10 2" stroke="#e6cf94" stroke-width="0.7"/></svg>lomivardell@quillmesh.net</li>
    </ul>
    <div class="person">
      <div class="person-name">Derek Holm</div>
      <div class="person-title">Operations Manager</div>
    </div>
  </section>

  <section class="card card--back">
    <div class="pattern" role="img" aria-label="Faint cream floral damask pattern"></div>
    <div class="brand-mark"></div>
    <div class="brand-name">Lomi Vardell</div>
    <div class="rule"></div>
    <div class="email-band">lomivardell@quillmesh.net</div>
  </section>

</body>
</html>
```